Hadley's Labouring Service needs a logo/business cards.

i've just started a new Labouring Business, Called Hadley's Labouring Service, I provide high quality labouring servicing to local Builders and Tradesmen.
I'd like my business cards to reflect the hard work and dedication I put into my business.
I'd like to see Burnt Orange and blacks in the cards and logo.
I want my cards to catch peoples eye as there is A lot of dull business cards in my industry.

Target Market(s)

Builders and other tradesmen

Contact Information for Business Card

Hadley's Labouring Service

Font styles to use
Sans Serif

Colors
f78f20
ffc214
000000
ffffff

Requirements
Must have
• My name : Tom Hadley
• My Number: 0497562083
• Email Address : hadleylabouringservice@examplemail.net
• A Sharp and Professional Design
Nice to have
• A unique design that separates my Cards from others,
• As I try to provide unique service to my clients I'd love my cards/logo to reflect this.

```html
<!DOCTYPE html>
<html lang="en">
<head>
<meta charset="utf-8">
<title>Hadley's Labouring Service – Business Card</title>
<link rel="stylesheet" href="https://fonts.googleapis.com/css2?family=Lato:wght@400;700&display=swap">
<style>
  :root {
    --burnt-orange: #f78f20;
    --card-black: #1c1c1c;
    --ink-black: #141414;
    --paper-white: #ffffff;
    --backdrop: #e9e6e3;
  }
  html, body {
    margin: 0;
    padding: 0;
    width: 1200px;
    height: 900px;
    overflow: hidden;
    background: var(--backdrop);
  }
  .canvas {
    position: relative;
    width: 1200px;
    height: 900px;
  }
  .business-card {
    position: absolute;
    left: 180px;
    top: 190px;
    width: 840px;
    height: 520px;
    background: var(--card-black);
    overflow: hidden;
    font-family: "Lato", Arial, sans-serif;
    box-shadow: 0 10px 30px rgba(0,0,0,0.18);
  }
  .accent-band {
    position: absolute;
    top: 0;
    right: 0;
    width: 266px;
    height: 100%;
    background: var(--burnt-orange);
  }
  .brand-disc {
    position: absolute;
    left: 358px;
    top: 32px;
    width: 446px;
    height: 446px;
    border-radius: 50%;
    background: radial-gradient(circle at 45% 40%, rgba(255,255,255,0.96), rgba(240,238,236,0.9));
    box-shadow: 0 4px 14px rgba(0,0,0,0.25);
  }
  .brand-mark {
    position: absolute;
    left: 147px;
    top: 58px;
    width: 152px;
    height: 152px;
    border-radius: 50%;
    background: var(--ink-black);
  }
  .brand-name {
    position: absolute;
    left: 0;
    right: 0;
    top: 238px;
    margin: 0;
    text-align: center;
    color: var(--burnt-orange);
    font-weight: 700;
    font-size: 34px;
    line-height: 1.2;
    letter-spacing: 1px;
    text-transform: uppercase;
  }
  .holder-name {
    position: absolute;
    left: 42px;
    top: 86px;
    margin: 0;
    color: var(--burnt-orange);
    font-weight: 700;
    font-size: 25px;
    letter-spacing: 0.3px;
    text-transform: uppercase;
  }
  .contact-details {
    position: absolute;
    left: 42px;
    top: 400px;
    margin: 0;
    color: var(--paper-white);
    font-weight: 400;
    font-size: 21px;
    line-height: 32px;
    font-style: normal;
  }
  .contact-details span { display: block; }
</style>
</head>
<body>
<div class="canvas">
  <section class="business-card">
    <div class="accent-band"></div>
    <h1 class="holder-name">Tom Hadley</h1>
    <div class="brand-disc">
      <div class="brand-mark"></div>
      <p class="brand-name">Hadley's<br>Labouring Service</p>
    </div>
    <address class="contact-details">
      <span class="phone">0497562083</span>
      <span class="email">hadleylabouringservice@examplemail.net</span>
    </address>
  </section>
</div>
</body>
</html>
```